Property Development Business Cards

I need a business card design for Tallow Creek Developments Pty Ltd. We are a property development company in Australia and our name defines the five values that we adhere to, being Profitable, Partnerships, Quality Developments, Eco Friendly and Enduring Design.

I have attached the current logo that I use, it is just five yellow circles connected to a single cricle in the middle.

Target Market(s)

Our Target audience is real estate agents, owners of properties, builders and other trades

Industry/Entity Type

Business

Requirements
Must have
• Want to have two sides to the card, one with details and one to just highlight the company

```html
<!DOCTYPE html>
<html lang="en">
<head>
<meta charset="utf-8">
<title>Tallow Creek Developments – Business Cards</title>
<link rel="stylesheet" href="https://fonts.googleapis.com/css2?family=Arimo:wght@400;700&family=Great+Vibes&display=swap">
<style>
  :root {
    --page: #ffffff;
    --orange: #f4b043;
    --cream: #f7dcb0;
    --yellow: #ffe81a;
    --brand-blue: #2a24d8;
    --ink: #1a1a1a;
    --signature: #3a3f8a;
    --card-shadow: rgba(0, 0, 0, 0.18);
    --mark-fill: #ffd76a;
  }
  * { box-sizing: border-box; margin: 0; padding: 0; }
  html, body { width: 1200px; height: 900px; overflow: hidden; background: var(--page); }
  .canvas {
    width: 1200px; height: 900px;
    display: flex; flex-direction: column; align-items: center; justify-content: center;
    gap: 36px;
  }
  .card {
    position: relative; width: 700px; height: 402px; background: #fff;
    box-shadow: 0 4px 16px var(--card-shadow); overflow: hidden;
    font-family: "Arimo", Arial, sans-serif;
  }
  .card__art { position: absolute; inset: 0; }
  .card__mark { position: absolute; }
  .front .card__mark { left: 58px; top: 108px; }
  .company {
    position: absolute; color: var(--brand-blue); font-weight: 700;
    text-align: center; line-height: 1.2;
  }
  .front .company { left: 250px; top: 70px; width: 430px; font-size: 30px; }
  .person { position: absolute; left: 250px; width: 430px; text-align: center; top: 176px; }
  .person__name {
    font-family: "Great Vibes", cursive; color: var(--signature); font-size: 34px; line-height: 1;
  }
  .person__role {
    font-size: 14px; letter-spacing: 3px; color: var(--ink); margin-top: 4px;
  }
  .web {
    position: absolute; color: var(--brand-blue); font-size: 12px;
  }
  .front .web { left: 282px; bottom: 22px; }
  .address {
    position: absolute; right: 28px; bottom: 22px; font-size: 12px; line-height: 1.35; color: var(--ink);
  }
  .back { background: var(--orange); }
  .back .company { left: 190px; top: 232px; width: 320px; font-size: 26px; }
  .back .card__mark { left: 310px; top: 110px; }
  .back .web { left: 0; right: 0; bottom: 14px; text-align: center; font-size: 18px; font-weight: 700; }
</style>
</head>
<body>
<main class="canvas">

  <section class="card front" aria-label="Business card front">
    <svg class="card__art" viewBox="0 0 700 402" aria-hidden="true">
      <path d="M0 0 H232 C184 90 188 250 330 402 H0 Z" fill="var(--yellow)"/>
      <path d="M0 0 H214 C166 90 170 250 302 402 H0 Z" fill="var(--cream)"/>
      <path d="M0 0 H192 C144 90 148 250 276 402 H0 Z" fill="var(--orange)"/>
    </svg>
    <svg class="card__mark" width="90" height="90" viewBox="0 0 90 90" role="img" aria-label="Company mark">
      <circle cx="45" cy="45" r="42" fill="var(--mark-fill)"/>
    </svg>
    <h1 class="company">Tallow Creek Developments<br>Pty Ltd</h1>
    <div class="person">
      <p class="person__name">Glen</p>
      <p class="person__role">Director</p>
    </div>
    <p class="web">www.tallowcreekdevelopments.com.au</p>
    <address class="address" style="font-style:normal">PO Box 718<br>Holt, ACT 2615</address>
  </section>

  <section class="card back" aria-label="Business card back">
    <svg class="card__art" viewBox="0 0 700 402" aria-hidden="true">
      <ellipse cx="350" cy="200" rx="186" ry="222" fill="var(--yellow)"/>
      <ellipse cx="350" cy="200" rx="174" ry="214" fill="var(--cream)"/>
      <ellipse cx="350" cy="200" rx="160" ry="206" fill="#ffffff"/>
    </svg>
    <svg class="card__mark" width="80" height="80" viewBox="0 0 80 80" role="img" aria-label="Company mark">
      <circle cx="40" cy="40" r="38" fill="var(--mark-fill)"/>
    </svg>
    <h2 class="company">Tallow Creek Developments<br>Pty Ltd</h2>
    <p class="web">www.tallowcreekdevelopments.com.au</p>
  </section>

</main>
</body>
</html>
```